Q-Rolls Business Card

We are a modern retail clothing store. Established in 1994. I need a presentable card that will amaze vendors when given to them.

Front: Logo in middle
Info Side:

Name: Tomas Velder
Cell: 630-812-4463
Work: 630-917-3384 EXT. 417
Email: Tomas@q-rolls-example.com
Website: www.Q-rolls-example.com

Industry/Entity Type

Business

```html
<!DOCTYPE html>
<html lang="en">
<head>
<meta charset="utf-8">
<title>Q-Rolls Business Card</title>
<link href="https://fonts.googleapis.com/css2?family=PT+Sans:wght@400;700&display=swap" rel="stylesheet">
<style>
  :root {
    --backdrop: #a2a2a2;
    --paper: #ffffff;
    --ink: #111111;
    --rule: #555555;
    --black-card: #000000;
    --reverse-ink: #ffffff;
  }
  html, body {
    margin: 0;
    padding: 0;
    width: 1200px;
    height: 900px;
    overflow: hidden;
    background: var(--backdrop);
    font-family: "PT Sans", Arial, sans-serif;
  }
  .stage {
    position: relative;
    width: 1200px;
    height: 900px;
  }
  .card {
    position: absolute;
    top: 275px;
    width: 477px;
    height: 294px;
    box-shadow: 0 10px 22px rgba(0,0,0,0.22);
    overflow: hidden;
  }
  .card--info {
    left: 116px;
    background: var(--paper);
    border-radius: 0 58px 0 58px;
  }
  .card--front {
    left: 622px;
    background: var(--black-card);
    border-radius: 58px 0 58px 0;
  }
  .wordmark {
    position: absolute;
    margin: 0;
    font-weight: 700;
    letter-spacing: 1px;
    line-height: 1;
    white-space: nowrap;
  }
  .card--info .wordmark {
    left: 18px;
    top: 46px;
    font-size: 72px;
    color: var(--ink);
  }
  .card--front .wordmark {
    left: 0;
    right: 0;
    top: 114px;
    text-align: center;
    font-size: 60px;
    color: var(--reverse-ink);
  }
  .name-rule {
    position: absolute;
    left: 0;
    right: 0;
    top: 158px;
    display: flex;
    align-items: center;
  }
  .name-rule::before,
  .name-rule::after {
    content: "";
    height: 1.5px;
    background: var(--rule);
  }
  .name-rule::before { flex: 1; }
  .name-rule::after { width: 22px; }
  .holder-name {
    padding: 0 9px 0 10px;
    font-size: 17px;
    font-weight: 700;
    color: var(--ink);
  }
  .contact-list {
    position: absolute;
    right: 30px;
    top: 193px;
    margin: 0;
    padding: 0;
    list-style: none;
    text-align: right;
  }
  .contact-list li {
    display: flex;
    justify-content: flex-end;
    align-items: center;
    gap: 5px;
    height: 20px;
    font-size: 13.5px;
    color: var(--ink);
  }
  .contact-list svg {
    width: 10px;
    height: 10px;
    flex: none;
  }
</style>
</head>
<body>
<main class="stage">
  <section class="card card--info" aria-label="Contact side">
    <h1 class="wordmark">Q-ROLLS</h1>
    <div class="name-rule"><span class="holder-name">Tomas Velder</span></div>
    <ul class="contact-list">
      <li>630-812-4463
        <svg viewBox="0 0 10 10" aria-hidden="true"><rect x="2.2" y="0.6" width="5.6" height="8.8" rx="1" fill="none" stroke="#111" stroke-width="1.2"/><rect x="4.2" y="7.4" width="1.6" height="0.9" fill="#111"/></svg>
      </li>
      <li>630-917-3384 EXT. 417
        <svg viewBox="0 0 10 10" aria-hidden="true"><path d="M2.3 0.8 L3.9 2.9 L3 4 Q4.1 6.1 6 7 L7.1 6.1 L9.2 7.7 L8.3 9.2 Q4.6 9.4 0.8 5 Q0.4 2.5 2.3 0.8 Z" fill="#111"/></svg>
      </li>
      <li>Tomas@q-rolls-example.com
        <svg viewBox="0 0 10 10" aria-hidden="true"><rect x="0.5" y="2" width="9" height="6.2" fill="#111"/><path d="M0.8 2.4 L5 5.6 L9.2 2.4" fill="none" stroke="#fff" stroke-width="0.9"/></svg>
      </li>
      <li>www.Q-rolls-example.com
        <svg viewBox="0 0 10 10" aria-hidden="true"><circle cx="5" cy="5" r="4.6" fill="#111"/><path d="M3 2.5 Q4.8 3 4.2 4.6 Q3 5.2 3.4 7 M6.2 1.4 Q7.8 3.6 6.4 5.2 Q6.8 7 8.2 7.4" fill="none" stroke="#fff" stroke-width="0.9"/></svg>
      </li>
    </ul>
  </section>

  <section class="card card--front" aria-label="Front side">
    <p class="wordmark">Q-ROLLS</p>
  </section>
</main>
</body>
</html>
```